Business Card design for consulting company

We are a small consulting company (Valmora Consulting) just starting out and need a business card design with a simple yet slick logo. We provide client focused consultancy support to manage and advise on procurement and acquisition projects for private businesses. Most of our projects are conducted for large well established companies and involve a fair degree of international work, so we would like to reflect that in the design. A large part of the business is also understanding client needs and then connecting them to, or sourcing the right solutions. So we would like to communicate our professionalism, an international focus and our willingness to provide tailored client solutions.

Target Market(s)

Generally we deal with middle to senior executive levels at large companies or with some high wealth private clients/companies. Mostly a conservative group so we want to project a sharp, professional and international image.

Industry/Entity Type

Consulting

Requirements
Must have
• Looking for a simple double sided business card design. Need to have our business name (Valmora Consulting), a person''s name and position title, and our company contact details. Also need a logo that would also convey the international nature of our consultancy.

```html
<!DOCTYPE html>
<html lang="en">
<head>
<meta charset="utf-8">
<title>Valmora Consulting – Business Card</title>
<link href="https://fonts.googleapis.com/css2?family=Open+Sans:ital,wght@0,400;0,600;0,700;1,700&display=swap" rel="stylesheet">
<style>
  :root {
    --ink: #3d3d3f;
    --steel-blue: #82b3c5;
    --steel-blue-pale: #e3ecf1;
    --paper: #ffffff;
    --card-edge: #d4d6d8;
    --text: #333436;
  }
  * { margin: 0; padding: 0; box-sizing: border-box; }
  html, body {
    width: 1200px;
    height: 901px;
    overflow: hidden;
    background: var(--paper);
    font-family: "Open Sans", Arial, sans-serif;
  }
  .sheet {
    position: relative;
    width: 1200px;
    height: 901px;
  }

  /* Wordmark: name in one colour and weight, with a plain globe dot beside it */
  .wordmark {
    position: absolute;
    display: flex;
    flex-direction: column;
    align-items: flex-end;
    font-weight: 700;
    line-height: 1;
  }
  .wordmark__row {
    display: flex;
    align-items: flex-start;
  }
  .wordmark__name { letter-spacing: -0.04em; }
  .wordmark__globe {
    width: 0.26em;
    height: 0.26em;
    border-radius: 50%;
    background: var(--steel-blue);
    margin-left: 0.06em;
    margin-top: 0.08em;
    flex: none;
  }
  .wordmark__tagline { letter-spacing: 0.14em; }

  .wordmark--hero {
    left: 150px;
    top: 150px;
    color: var(--ink);
    font-size: 112px;
  }
  .wordmark--hero .wordmark__tagline { font-size: 30px; margin-top: 8px; }

  /* Front of card */
  .card-front {
    position: absolute;
    left: 23px;
    top: 456px;
    width: 739px;
    height: 426px;
    background: var(--steel-blue);
    overflow: hidden;
  }
  .card-front .wordmark {
    left: 258px;
    top: 170px;
    color: var(--paper);
    font-size: 50px;
  }
  .card-front .wordmark__globe { background: var(--ink); }
  .card-front .wordmark__tagline { font-size: 15px; margin-top: 4px; }

  /* Back of card */
  .card-back {
    position: absolute;
    left: 775px;
    top: 143px;
    width: 423px;
    height: 739px;
    background: var(--paper);
    border: 2px solid var(--card-edge);
    overflow: hidden;
  }
  .card-back .wordmark {
    right: 34px;
    top: 268px;
    color: var(--ink);
    font-size: 50px;
  }
  .card-back .wordmark__tagline { font-size: 15px; margin-top: 4px; }

  .contact {
    position: absolute;
    right: 34px;
    top: 432px;
    text-align: right;
    color: var(--text);
    font-style: normal;
  }
  .contact__name {
    font-size: 21px;
    font-weight: 700;
    font-style: italic;
    letter-spacing: 0.12em;
  }
  .contact__title {
    font-size: 17px;
    letter-spacing: 0.06em;
    margin-top: 12px;
  }
  .contact__lines {
    list-style: none;
    margin-top: 46px;
    font-size: 17px;
    letter-spacing: 0.1em;
    line-height: 39px;
  }
</style>
</head>
<body>
  <main class="sheet">
    <div class="wordmark wordmark--hero">
      <div class="wordmark__row">
        <span class="wordmark__name">valmora</span>
        <span class="wordmark__globe" aria-hidden="true"></span>
      </div>
      <span class="wordmark__tagline">CONSULTING</span>
    </div>

    <section class="card-front" aria-label="Card front">
      <div class="wordmark">
        <div class="wordmark__row">
          <span class="wordmark__name">valmora</span>
          <span class="wordmark__globe" aria-hidden="true"></span>
        </div>
        <span class="wordmark__tagline">CONSULTING</span>
      </div>
    </section>

    <section class="card-back" aria-label="Card back">
      <div class="wordmark">
        <div class="wordmark__row">
          <span class="wordmark__name">valmora</span>
          <span class="wordmark__globe" aria-hidden="true"></span>
        </div>
        <span class="wordmark__tagline">CONSULTING</span>
      </div>
      <address class="contact">
        <p class="contact__name">Your Name</p>
        <p class="contact__title">Job Title</p>
        <ul class="contact__lines">
          <li>p (555) 555-5555</li>
          <li>f (555) 555-5555</li>
          <li>yourname@valmora.com</li>
        </ul>
      </address>
    </section>
  </main>
</body>
</html>
```